Wild Mo's Wine Label Project

We need a new entry level wine label called "Wild Mo's" for a range of wines we are developing from inland Australia. Our company is made up of three youngish guys who live hard and love taking the mickey. Wild Mo is Wild Moss - the largest and loudest of the three partners (and ideally this label will take the mickey out of him). We've grown the grapes ourselves for this first release which will be a 2012 Pinot Gris. Wine style is dry, young, fresh and contemporary and pitched at the sub AUD $10 retail price point. The package will be flint (clear) claret shape bottle with plain screwcap (colour matched to suit the winning label design).

I've attached a couple of photos of Wild Moss to give you some idea of his presence and persona.

Target Market(s)

Semi educated 25 - 40 year old wine drinkers. Skewed towards females.

Industry/Entity Type

Retail

Requirements
Should not have
• Anything traditional or old fashioned

```html
<!DOCTYPE html>
<html lang="en">
<head>
<meta charset="utf-8">
<title>Wild Mo Pinot Gris 2012 Label</title>
<link rel="stylesheet" href="https://fonts.googleapis.com/css2?family=Questrial&family=Poiret+One&display=swap">
<style>
  :root {
    --page: #ffffff;
    --label-black: #000000;
    --ink-white: #ffffff;
    --teal: #1f8a9a;
    --gold: #b59a4a;
    --olive: #9aa257;
    --band-dark: #3a3a3a;
    --band-light: #9c9c9c;
    --wine-red: #8e1b1b;
    --detail-ink: #2e2e2e;
  }
  html, body {
    margin: 0;
    width: 1200px;
    height: 982px;
    overflow: hidden;
    background: var(--page);
  }
  .canvas {
    position: relative;
    width: 1200px;
    height: 982px;
  }
  .label {
    position: absolute;
    left: 275px;
    top: 58px;
    width: 650px;
    height: 865px;
    background: var(--label-black);
    box-shadow: 10px 10px 14px rgba(0, 0, 0, 0.35);
    overflow: hidden;
    font-family: "Questrial", sans-serif;
  }
  .label-art {
    position: absolute;
    inset: 0;
  }
  .brand {
    position: absolute;
    left: 40px;
    top: 22px;
    display: flex;
    align-items: center;
    gap: 22px;
    color: var(--ink-white);
  }
  .brand-name {
    font-size: 100px;
    line-height: 1;
    letter-spacing: 1px;
  }
  .brand-dot {
    width: 96px;
    height: 96px;
    border-radius: 50%;
    background: var(--ink-white);
  }
  .varietal {
    position: absolute;
    left: 40px;
    top: 378px;
    margin: 0;
    font-family: "Poiret One", sans-serif;
    font-weight: 400;
    font-size: 104px;
    line-height: 1;
    word-spacing: 40px;
    white-space: nowrap;
    color: var(--ink-white);
  }
  .vintage {
    position: absolute;
    left: 392px;
    top: 582px;
    font-size: 58px;
    letter-spacing: 14px;
    color: var(--ink-white);
    font-weight: 700;
  }
  .info-band {
    position: absolute;
    left: 0;
    top: 689px;
    width: 100%;
    height: 118px;
    background: linear-gradient(180deg, var(--band-dark) 0%, #4a4a4a 45%, var(--band-light) 62%, #8a8a8a 100%);
    text-align: center;
  }
  .producer {
    margin: 8px 0 0;
    font-size: 58px;
    font-variant: small-caps;
    letter-spacing: 3px;
    line-height: 1;
    color: var(--wine-red);
  }
  .details {
    margin: 10px 0 0;
    font-size: 38px;
    line-height: 1;
    color: var(--detail-ink);
  }
  .details .dot {
    color: var(--wine-red);
  }
</style>
</head>
<body>
<main class="canvas">
  <section class="label">
    <svg class="label-art" width="650" height="865" viewBox="0 0 650 865">
      <defs>
        <linearGradient id="drop-tones" x1="0" y1="0" x2="1" y2="1">
          <stop offset="0" stop-color="#1f8a9a"/>
          <stop offset="0.5" stop-color="#b59a4a"/>
          <stop offset="1" stop-color="#9aa257"/>
        </linearGradient>
      </defs>
      <rect class="drop-artwork" x="100" y="140" width="372" height="416" rx="120"
            fill="url(#drop-tones)" opacity="0.85"
            role="img" aria-label="Decorative teal and gold droplet leaf shapes"/>
      <path class="swoosh" fill="none" stroke="#ffffff" stroke-width="28"
            d="M130 865 Q154 330 650 190"/>
    </svg>

    <div class="brand">
      <span class="brand-name">WILD MO</span>
      <span class="brand-dot"></span>
    </div>

    <h1 class="varietal">Pinot Gris</h1>
    <div class="vintage">2012</div>

    <div class="info-band">
      <p class="producer">Amber Thursday</p>
      <p class="details">Alcohol 12% By Volume <span class="dot">●</span> 750ml</p>
    </div>
  </section>
</main>
</body>
</html>
```